crumbs of morning project

I need 2 stickers (lid and side) for a see-through rectangular plastic container that holds a whole, free range chicken.
Updates

CHANGE OF PACKAGING

 

we are unable to source the clear, rectangular, see-throughcontainer in the previously attached file and have to amend our packagingstrategy.

 

 

 

UPDATED STRATEGY:

 

we intend to use one of the 'french style' cardboard typewrap-around stickers as shown in the new attachments I have posted. australiansupermarkets would not accept this type of thin cardboard on its own as is applicablein france and for that reason we intend insert the wrapped-around cardboard stickeredwhole chicken on a poly styrene tray and then placed in a clear plastic cellophanebag with a twisted tie as shown the 'varnot brand' attached file.

 

the other technical requirements (barcode, kilograms, netpricing, etc.) remain the same

 

 

also note:

 

when using our existing 'seal pure' logo, please removethe text:

 

rabbi tovah lindquist haber

potential brand names:

1. crumbs of morning
2. brisk olando

cardboard label needs to be a ' wrap around label' (wrapped, north-south) as shown in the following 
attached files:

'wrap around label'  + 'wrap around label b'

we like the 'brisk olando' FONT and primary yellow background. 

dorvid 

Target Market(s)

free range poultry consumers (GREENIES) jews (seal pure), affluent, up market, product is priced at the premium end of the market

Industry/Entity Type

Plastic

Requirements
Must have
• in order of importance...

LID LABEL STICKER-(see attached photo)
logo name (crumbs of morning)
free range
sanitised with kosher rock salt
extra fresh
long shelf life
kosher certified

SIDE LABEL STICKER- (see attached photo)
country of manufacture
processors contact details
(7 pellbrook lane ashvale west 3290 0487 220 318 www.crumbsofmorning.com.au)
barcode
product description (whole, drumsticks, filets, etc)
kosher status declaration and kosher logo (see attachment)
price per kilogram section
net weight per kilogram section
use by date
total price
refrigeration advise-store below 5degreesC

note:

the whole chicken is wrapped in light BROWN colored butchers paper and tied with a green ribbon. the customer can only see the raw chicken at each end.

```html
<!DOCTYPE html>
<html lang="en">
<head>
<meta charset="utf-8">
<title>Crumbs Of Morning – Lid Label</title>
<link rel="stylesheet" href="https://fonts.googleapis.com/css2?family=Jost:wght@400&family=Roboto+Slab:wght@800&display=swap">
<style>
  :root {
    --edge: #f2f2f2;
    --frame: #9a9a9a;
    --orange-deep: #e8793a;
    --orange-mid: #eea23a;
    --yellow-glow: #f6dc00;
    --panel: #211d1b;
    --panel-text: #ffffff;
    --body-text: #2a211a;
  }
  * { box-sizing: border-box; margin: 0; padding: 0; }
  html, body {
    width: 1200px;
    height: 900px;
    overflow: hidden;
    background: var(--edge);
  }
  .label {
    position: absolute;
    left: 8px;
    top: 8px;
    width: 1184px;
    height: 884px;
    border: 1px solid var(--frame);
    background:
      radial-gradient(ellipse 620px 520px at 590px 540px,
        var(--yellow-glow) 0%,
        var(--orange-mid) 40%,
        var(--orange-mid) 62%,
        var(--orange-deep) 100%);
    overflow: hidden;
  }
  .brand-panel {
    position: absolute;
    left: 354px;
    top: 0;
    width: 476px;
    height: 515px;
    background: var(--panel);
    color: var(--panel-text);
    text-align: center;
  }
  .brand-top {
    position: absolute;
    left: 0;
    right: 0;
    top: 335px;
    font-family: "Jost", sans-serif;
    font-weight: 400;
    font-size: 49px;
    letter-spacing: 4px;
    line-height: 1;
  }
  .brand-rule {
    position: absolute;
    left: 40px;
    width: 396px;
    top: 400px;
    height: 4px;
    background: var(--panel-text);
  }
  .brand-main {
    position: absolute;
    left: 0;
    right: 0;
    top: 414px;
    font-family: "Roboto Slab", serif;
    font-weight: 800;
    font-size: 58px;
    line-height: 1;
    letter-spacing: 0;
  }
  .claims {
    position: absolute;
    left: 0;
    right: 0;
    top: 651px;
    list-style: none;
    text-align: center;
    font-family: "Jost", sans-serif;
    font-size: 35px;
    line-height: 46px;
    color: var(--body-text);
  }
</style>
</head>
<body>
  <main class="label">
    <section class="brand-panel">
      <p class="brand-top">CRUMBS OF</p>
      <div class="brand-rule"></div>
      <p class="brand-main">MORNING</p>
    </section>
    <ul class="claims">
      <li>Free Range</li>
      <li>Sanitised with Kosher Rock Salt</li>
      <li>Extra Fresh</li>
      <li>Long Shelf Life</li>
      <li>Kosher Certified</li>
    </ul>
  </main>
</body>
</html>
```